Medical equipment business looking for professional, unique business card

We need a business card design for a durable medical equipment company. We are small but would like our cards to express that we are much bigger. We focus on braces (back, knee, wrist, etc) but also do crutches, rollators, wheelchairs- basically medical equipment that gets you going and back in Action. Our colors are blue and green and our logo has an arrow and use of a "spine". We'd like to express professionalism while being unique.

Industry/Entity Type

Medical Equipment

Contact Information for Business Card

Professional feel but unique. Memorable.

Font styles to use
Serif
Sans Serif
Other font styles liked:
• verdana

Requirements
Must have
• card holders cell#, business phone#, fax#, email, website address, business address, logo
Nice to have
• use of medical/healthcare related descriptive words, items, look
Should not have
• the wrong colors or cartoon characters.

```html
<!DOCTYPE html>
<html lang="en">
<head>
<meta charset="utf-8">
<title>Stride DME – Business Card</title>
<link rel="stylesheet" href="https://fonts.googleapis.com/css2?family=Noto+Sans:wght@400;700&display=swap">
<style>
  :root {
    --page-bg: #e6e2dc;
    --card-light: #f4f5f4;
    --card-mid: #dfe5e8;
    --brand-navy: #163650;
    --brand-green: #6aaa3a;
    --brand-blue: #1f6ea6;
    --text-dark: #2b3b4b;
    --web-text: #b9c5cd;
  }
  * { margin: 0; padding: 0; box-sizing: border-box; }
  html, body { width: 1200px; height: 970px; overflow: hidden; }
  body {
    background: var(--page-bg);
    font-family: "Noto Sans", Verdana, sans-serif;
    position: relative;
  }
  .card {
    position: absolute;
    left: 80px; top: 189px;
    width: 1040px; height: 592px;
    background: linear-gradient(135deg, var(--card-light) 0%, var(--card-mid) 100%);
    overflow: hidden;
    box-shadow: 0 10px 30px rgba(0,0,0,.18);
  }
  .card-shapes { position: absolute; inset: 0; }
  .brand { position: absolute; left: 620px; top: 88px; }
  .brand-name {
    font-size: 62px; font-weight: 700; color: var(--brand-navy);
    line-height: 1; letter-spacing: -1px;
  }
  .brand-tagline {
    margin-top: 18px; font-size: 23px; font-weight: 700;
    color: var(--brand-blue); line-height: 1;
  }
  .holder { position: absolute; left: 48px; top: 222px; }
  .holder-name {
    font-size: 34px; font-weight: 700; color: var(--brand-navy);
    letter-spacing: 1px; line-height: 1.1;
  }
  .holder-title { font-size: 27px; color: var(--brand-green); line-height: 1.2; letter-spacing: .5px; }
  .address {
    position: absolute; left: 46px; top: 322px;
    font-size: 27px; color: var(--text-dark); line-height: 35px;
  }
  .contacts {
    position: absolute; left: 48px; top: 410px;
    list-style: none; font-size: 27px; color: var(--text-dark); line-height: 36.5px;
  }
  .contacts li { display: flex; align-items: center; gap: 14px; }
  .contacts svg { width: 30px; height: 30px; flex: none; }
  .website {
    position: absolute; right: 48px; top: 532px;
    font-size: 25px; color: var(--web-text); letter-spacing: 1px;
  }
</style>
</head>
<body>
  <div class="card">
    <svg class="card-shapes" viewBox="0 0 1040 592" width="1040" height="592">
      <path d="M0 0 H1040 V8 C760 4 560 10 400 30 C210 60 80 130 0 225 Z" fill="var(--brand-green)"/>
      <path d="M1040 235 C960 380 760 500 420 535 C260 552 120 556 0 556 V592 H1040 Z" fill="var(--brand-navy)"/>
    </svg>

    <div class="brand">
      <div class="brand-name">Stride DME</div>
      <div class="brand-tagline">Durable Medical Equipment</div>
    </div>

    <div class="holder">
      <div class="holder-name">EMPLOYEE NAME</div>
      <div class="holder-title">Managing Director</div>
    </div>

    <div class="address">PO BOX&nbsp; 123 your address,<br>2nd street london ,USA</div>

    <ul class="contacts">
      <li>
        <svg viewBox="0 0 30 30" aria-hidden="true"><rect width="30" height="30" fill="var(--brand-green)"/><path d="M7 13 C7 8 23 8 23 13 L20 14 L19 11 H11 L10 14 Z M9 16 H21 L23 23 H7 Z" fill="#fff"/></svg>
        <span>(01) 2345 6789</span>
      </li>
      <li>
        <svg viewBox="0 0 30 30" aria-hidden="true"><rect width="30" height="30" fill="var(--brand-green)"/><rect x="9" y="5" width="12" height="7" fill="#fff"/><rect x="6" y="12" width="18" height="9" fill="#fff"/><rect x="9" y="19" width="12" height="6" fill="#fff" stroke="var(--brand-green)" stroke-width="1"/></svg>
        <span>(01) 2345 6789</span>
      </li>
      <li>
        <svg viewBox="0 0 30 30" aria-hidden="true"><rect width="30" height="30" fill="var(--brand-green)"/><rect x="5" y="8" width="20" height="14" fill="#fff"/><path d="M5 8 L15 16 L25 8" fill="none" stroke="var(--brand-green)" stroke-width="1.5"/></svg>
        <span>Info@yourcompany.com</span>
      </li>
    </ul>

    <div class="website">www.yourcompany.com</div>
  </div>
</body>
</html>
```